Tallowin geriatric care need letterhead design

Please help to design a letterhead document which will will be used as correspondent letter to other doctors.

apart from designing the letterhead, please also do the arrangement for the format so that it can be ready to use.

Please allocate page number at the bottom of the letter and also, small print for Tallowin geriatric care on the bottom of the page.
the template will need to be workable on word document so that the letter can be typed out with perfect match.

Format :
17th July 2104
To: Dr.xxx
Address.........

Re: Mr. NNN
Address
DOB

Dear Dr XXX,

Kind regards,

Dr. SSS
Provider no. 8592043

I do not have a physical address, tel or fax currently so, please allocated specific area for the company detail.

There will be up to 3 address on the letter with one of it been the main address

Eg.
Main Room--address
other consultation address

Thank you

Dear all designers, Please help to design the letter head. don't worry about the previous brief. use your imagination and no need to worry about the patient detail etc. The following information need to be in the letterhead Main room Suite 6.14 Norvu Medical 241-243 Corbel Street Orrin Hill VIC 3462 Phone: Fax: Peripheral room: Kelvindale Medical Centre street, kelvindale VIC 3417 Our Lady of Pemberly, 4718 dunmarra road, franskton vic 3199 Quenton Private specialist clinic, 867 pelliton road, mt. pelliton vic 3409 please put in the ABN: 690371 which is the company registration no. ( in a small font as it doesn't need to bed obvious) somewhere on the top.

```html
<!DOCTYPE html>
<html lang="en">
<head>
<meta charset="utf-8">
<title>Tallowin Geriatric Care – Letterhead</title>
<link rel="stylesheet" href="https://fonts.googleapis.com/css2?family=Libre+Baskerville&family=Montserrat:wght@500&family=Roboto+Condensed:wght@400;700&display=swap">
<style>
  :root {
    --backdrop: #e9e9ea;
    --paper: #ffffff;
    --navy: #2a3768;
    --red: #c41f2e;
    --grey: #8a8d96;
  }
  html, body {
    margin: 0;
    width: 1200px;
    height: 943px;
    overflow: hidden;
    background: var(--backdrop);
  }
  .letterhead {
    position: absolute;
    left: 289px;
    top: 32px;
    width: 622px;
    height: 879px;
    background: var(--paper);
    box-shadow: 0 2px 10px rgba(0,0,0,0.12);
  }
  .brand {
    position: absolute;
    left: 44px;
    top: 46px;
    display: flex;
    align-items: center;
    gap: 10px;
  }
  .brand-dot {
    width: 22px;
    height: 22px;
    border-radius: 50%;
    background: var(--red);
  }
  .brand-name {
    font-family: "Libre Baskerville", Georgia, serif;
    font-size: 24px;
    color: var(--navy);
    line-height: 1;
  }
  .brand-tagline {
    font-family: "Montserrat", Arial, sans-serif;
    font-weight: 500;
    font-size: 8px;
    letter-spacing: 5px;
    color: var(--grey);
    margin-top: 5px;
    text-transform: uppercase;
  }
  .locations {
    position: absolute;
    left: 0;
    right: 24px;
    bottom: 40px;
    margin: 0;
    padding: 0;
    list-style: none;
    font-family: "Roboto Condensed", Arial, sans-serif;
    font-weight: 700;
    font-size: 9.4px;
    color: var(--navy);
  }
  .location {
    display: flex;
    align-items: center;
    margin-top: 3px;
    white-space: nowrap;
  }
  .location-label {
    background: var(--red);
    color: var(--paper);
    padding: 2px 6px 2px 10px;
    margin-right: 4px;
    text-transform: uppercase;
    clip-path: polygon(0 0, 100% 0, calc(100% - 5px) 100%, 0 100%);
  }
  .abn {
    position: absolute;
    right: 24px;
    bottom: 28px;
    font-family: "Roboto Condensed", Arial, sans-serif;
    font-size: 6.5px;
    color: var(--grey);
  }
</style>
</head>
<body>
  <main class="letterhead">
    <header class="brand">
      <span class="brand-dot"></span>
      <div>
        <div class="brand-name">Tallowin Geriatric Care</div>
        <div class="brand-tagline">Caring with respect</div>
      </div>
    </header>

    <ul class="locations">
      <li class="location">
        <span class="location-label">Main Room:</span>
        Suite 6.14, Norvu Medical 241-243 Corbel Street Orrin Hill VIC 3462 Phone: 007731842 Fax: 007731843
      </li>
      <li class="location">
        <span class="location-label">Peripheral Room:</span>
        Kelvindale Medical Centre street, kelvindale VIC 3417 Our Lady of Pemberly 4718 dunmarra road, dunmarra vic 3288 Quenton
      </li>
      <li class="location">
        <span class="location-label">Private Specialist Clinic:</span>
        867 pelliton road, mt. pelliton vic 3409
      </li>
    </ul>
    <div class="abn">ABN: 690371</div>
  </main>
</body>
</html>
```